Website Design for VELKA Consulting

VELKA offers consulting advice to companies seeking grants, government concessions, and other funding sources for research and development. Our clients vary in size from small start-up companies, to international corporations with billions of dollars in an

```html
<!DOCTYPE html>
<html lang="en">
<head>
<meta charset="utf-8">
<title>VELKA Consulting</title>
<link rel="stylesheet" href="https://fonts.googleapis.com/css2?family=PT+Sans+Narrow:wght@400;700&family=Arimo:wght@400;700&display=swap">
<style>
:root{
  --orange:#c8541f;
  --orange-text:#c45a24;
  --ink:#1a1a1a;
  --body:#333333;
  --band:#e2e2e2;
  --welcome:#f0f0f0;
  --footer:#000000;
  --head:"PT Sans Narrow",sans-serif;
  --text:"Arimo",sans-serif;
}
*{margin:0;padding:0;box-sizing:border-box}
html,body{width:960px;height:1200px;overflow:hidden;background:var(--footer)}
.page{position:relative;width:960px;height:1200px;font-family:var(--text);color:var(--body)}
.nav{position:absolute;left:0;top:0;width:960px;height:46px;background:linear-gradient(#262626,#141414);display:flex;justify-content:center;gap:19px;padding-left:20px;align-items:center}
.nav a{font-family:var(--head);color:#f2f2f2;font-size:13.5px;text-decoration:none}
.hero{position:absolute;left:0;top:46px;width:960px;height:395px;background:radial-gradient(ellipse at 30% 35%,#d9d9d9,#9a9a9a 45%,#5b5b5b 80%,#3d3d3d)}
.brand{position:absolute;left:194px;top:66px;display:flex;align-items:center;gap:8px;font-family:var(--head);font-weight:700;font-size:34px;color:#2a2a2a;letter-spacing:.5px}
.brand .mark{width:40px;height:40px;background:var(--orange)}
.social-tab{position:absolute;left:661px;top:46px;width:103px;height:31px;background:rgba(220,220,220,.85);display:flex;gap:10px;justify-content:center;align-items:center}
.sq{width:17px;height:17px;border-radius:3px;background:#8a8a8a}
.hero-panel{position:absolute;left:373px;top:151px;width:376px;height:208px;background:rgba(200,200,200,.78);padding:12px 18px 0 25px}
.hero-panel h1{font-family:var(--head);font-weight:700;color:var(--orange-text);font-size:38px;line-height:40px}
.hero-panel h2{font-family:var(--head);font-weight:400;color:var(--ink);font-size:14px;margin-top:6px}
.hero-panel p{font-size:8.1px;line-height:13px;color:#1f1f1f;margin-top:4px}
.btn{display:inline-block;font-family:var(--head);font-weight:700;font-size:10px;color:#fff;padding:3px 8px;background:var(--ink);text-decoration:none}
.btn.orange{background:var(--orange)}
.hero-panel .more{text-align:right;margin-top:9px;padding-right:6px}
.hero-panel .btn{font-size:10.5px}
.dots{position:absolute;left:439px;top:401px;display:flex;gap:6px}
.dots span{width:12px;height:12px;border-radius:50%;border:2px solid #fff}
.dots span.on{background:var(--orange);border-color:var(--orange)}
.services{position:absolute;left:0;top:441px;width:960px;height:222px;background:var(--band)}
.service{position:absolute;top:22px;width:150px}
.service .icon{position:absolute;left:-33px;top:0}
.service h3{font-family:var(--head);font-weight:700;font-size:16px;line-height:19px;color:var(--ink);text-transform:uppercase;border-bottom:1px solid var(--ink);padding-bottom:2px;min-height:41px}
.service.feature h3{color:var(--orange-text);border-color:var(--orange-text)}
.service p{font-size:8.1px;line-height:11px;margin-top:11px;color:var(--body)}
.service.feature p{color:var(--orange-text)}
.service .btn{position:absolute;top:164px;left:0}
.welcome{position:absolute;left:0;top:663px;width:960px;height:238px;background:var(--welcome)}
.intro{position:absolute;left:192px;top:22px;width:373px}
.intro h2,.news h2{font-family:var(--head);font-weight:700;font-size:16px;color:var(--ink);border-bottom:1px solid var(--ink);padding-bottom:1px}
.intro p{font-size:7.9px;line-height:10px;margin-top:9px;color:var(--body)}
.intro .tagline{font-family:var(--head);font-weight:700;color:var(--orange-text);font-size:13px;margin:5px 0 0 132px;line-height:14px}
.news{position:absolute;left:631px;top:22px;width:133px}
.news h4{font-size:8.1px;font-weight:400;color:var(--orange-text);margin-top:11px;padding-left:10px;position:relative}
.news h4::before{content:"";position:absolute;left:0;top:1px;width:5px;height:5px;border:1px solid var(--orange-text);border-radius:50%}
.news p{font-size:7.8px;line-height:10px;padding-left:10px;margin-top:4px;color:var(--body)}
.news .item+.item h4{margin-top:16px}
.footer{position:absolute;left:0;top:901px;width:960px;height:299px;background:var(--footer);color:#e6e6e6}
.footer .brand{left:202px;top:23px;color:#eeeeee;font-size:32px}
.footer .copy{position:absolute;left:198px;top:76px;font-size:8.3px}
.footer address{position:absolute;left:367px;top:27px;font-style:normal;font-size:8.3px;line-height:11px;border-left:1px solid #888;padding-left:8px;height:75px}
.footer address .gap{margin-top:10px}
.footer .social{position:absolute;left:660px;top:30px;display:flex;gap:9px}
.footer .social .sq{width:18px;height:18px;background:#7c7c7c}
</style>
</head>
<body>
<div class="page">
  <nav class="nav">
    <a href="#">Home</a><a href="#">About us</a><a href="#">Funding opportunities</a><a href="#">Services</a><a href="#">Carbon footprint</a><a href="#">Management team</a><a href="#">News</a><a href="#">Contact</a>
  </nav>

  <header class="hero" role="img" aria-label="Black and white photograph of wind turbines against a cloudy sky"></header>
  <div class="brand"><span class="mark"></span>VELKA</div>
  <div class="social-tab"><span class="sq"></span><span class="sq"></span><span class="sq"></span></div>

  <section class="hero-panel">
    <h1>Investing in your business?</h1>
    <h2>Government incentives are available to offset these costs.</h2>
    <p>VELKA offers a tailored compliance service, adapted to your company's requirements, culture, and operating conditions. We work 1-on-1 with your technical and financial staff, visiting your sites regardless of their location, and ensuring that strong relationships are built and maximum value is extracted from the R&amp;D projects you undertake.</p>
    <div class="more"><a class="btn orange" href="#">Read more</a></div>
  </section>
  <div class="dots"><span class="on"></span><span></span><span></span><span></span><span></span></div>

  <section class="services">
    <article class="service feature" style="left:226px">
      <svg class="icon" width="26" height="24" viewBox="0 0 26 24"><rect x="3" y="2" width="12" height="6" transform="rotate(35 9 5)" fill="#c8541f"/><rect x="10" y="6" width="3" height="12" transform="rotate(-55 11.5 12)" fill="#c8541f"/><rect x="0" y="19" width="16" height="4" fill="#c8541f"/></svg>
      <h3>R&amp;D Tax Concession/Incentive</h3>
      <p>VELKA offers a tailored compliance service, adapted to your company's requirements, culture, and operating conditions. We work 1-on-1 with your technical and financial staff, visiting your sites regardless of their location, and ensuring that strong relationships are built and maximum value is extracted from the R&amp;D projects you undertake</p>
      <a class="btn orange" href="#">Read more</a>
    </article>
    <article class="service" style="left:431px">
      <svg class="icon" width="20" height="22" viewBox="0 0 20 22"><rect width="20" height="22" rx="2" fill="#1a1a1a"/><rect x="3" y="3" width="14" height="5" fill="#e2e2e2"/><g fill="#e2e2e2"><rect x="3" y="10" width="3" height="3"/><rect x="8.5" y="10" width="3" height="3"/><rect x="14" y="10" width="3" height="3"/><rect x="3" y="16" width="3" height="3"/><rect x="8.5" y="16" width="3" height="3"/><rect x="14" y="16" width="3" height="3"/></g></svg>
      <h3>Grant and Funding Applications</h3>
      <p>The Federal Government offers a wide variety of grants and loans to businesses of different sizes. Funding is highly sought after and applications are extremely competitive, which is where VELKA's extensive experience in drafting and reviewing applications can significantly improve the likelihood of your application being successful.</p>
      <a class="btn" href="#">Read more</a>
    </article>
    <article class="service" style="left:635px">
      <svg class="icon" width="28" height="22" viewBox="0 0 28 22"><path d="M0 6 L7 2 L14 8 L21 2 L28 6 L24 14 L16 21 L12 21 L4 14 Z" fill="#1a1a1a"/></svg>
      <h3>Audit &amp; Review</h3>
      <p>From time to time, Tax Concession applications may be reviewed by regulatory bodies to ensure they comply with the program's guidelines. The VELKA team possesses extensive experience in managing such reviews, and facilitating discussions with government representatives to ensure the arguments for your claim are clearly and accurately articulated</p>
      <a class="btn" href="#">Read more</a>
    </article>
  </section>

  <section class="welcome">
    <div class="intro">
      <h2>WELCOME TO VELKA CONSULTING</h2>
      <p>VELKA Consulting is a Sydney-based consulting company with customers across Australia, operating in a wide range of industries.</p>
      <p>We aim to deliver maximum value to all of our clients, by identifying tax concessions and funding opportunities for seemingly everyday tasks, such as process improvement initiatives and product development activities.</p>
      <p>Since 2003, VELKA has received widespread accolades from its clients, including many Top 500 companies, for its hands-on approach, out-of-the-box thinking, and “why not?” attitude.</p>
      <p>Our philosophy is simple; what is the best possible outcome for the customer, and how can we deliver it? Often, this means breaking away from traditional and antiquated consulting methodologies and devising a more customized and focused approach.</p>
      <p>Achieving goals is good, exceeding them is great.</p>
      <p class="tagline">Think great. Think VELKA.</p>
    </div>
    <aside class="news">
      <h2>NEWS</h2>
      <div class="item">
        <h4>Senate Passes R&amp;D Tax Credit</h4>
        <p>Earlier today, the highly debated R&amp;D Tax Credit Bill was passed by the Senate, after more than two years of debate and subsequent amendment.</p>
      </div>
      <div class="item">
        <h4>Green Light for R&amp;D Tax Credit</h4>
        <p>The Government has announced it has achieved cross-bench support for the proposed R&amp;D Tax Credit legislation.</p>
      </div>
    </aside>
  </section>

  <footer class="footer">
    <div class="brand"><span class="mark"></span>VELKA</div>
    <div class="copy">© 2013 | PRIVACY POLICY</div>
    <address>
      VELKA Consulting Pty. Ltd.<br>Level 4, 58 Harbour Lane<br>Northgate N.S.W. 2199
      <div class="gap">P:&nbsp;&nbsp; +61 2 5550 0100<br>F:&nbsp;&nbsp; +61 2 5550 0400<br>E:&nbsp;&nbsp; info@velkaconsulting.example</div>
    </address>
    <div class="social"><span class="sq"></span><span class="sq"></span><span class="sq"></span><span class="sq"></span></div>
  </footer>
</div>
</body>
</html>
```